Product Insert / Thank You

I'm looking for a small card to be designed that will be included with our product when it ships. It will be 2 sided with 1 side being a "thank you" with our logo and the other side containing the following text:We would love to hear your feedback! For every review we receive on our products, we donate 100% of the proceeds of your order to TIDEWELL -- a non profit organization dedicated to preserving our oceans!If you are not 100% satisfied with your purchase or have any problems, we will always resolve your issue. please contact us via Brindle if you need assistance.Insert needs to be well organized and information presented in a clear and visually appealing way.
Target Market(s)
Women, aged 24-45
Colors
Designer to choose colors to be used in the design.
Look and feel

```html
<!DOCTYPE html>
<html lang="en">
<head>
<meta charset="utf-8">
<title>Ridgeway – Thank You Insert</title>
<link href="https://fonts.googleapis.com/css2?family=Great+Vibes&family=Lato:wght@300;700;900&display=swap" rel="stylesheet">
<style>
  :root {
    --deep-blue: #1077be;
    --sky-blue: #29a8e0;
    --pale-blue: #d7e8f7;
    --ink-blue: #2a9fd8;
    --white: #ffffff;
  }
  * { box-sizing: border-box; margin: 0; padding: 0; }
  html, body {
    width: 1200px; height: 900px; overflow: hidden;
    background: var(--white);
    font-family: "Lato", sans-serif;
  }
  .canvas { position: relative; width: 1200px; height: 900px; }

  .card {
    position: absolute;
    width: 541px; height: 378px;
    background: var(--pale-blue);
    overflow: hidden;
  }
  .card--front { left: 340px; top: 33px; }
  .card--back  { left: 338px; top: 462px; }

  .pattern-band {
    position: absolute; left: 0; width: 100%;
    background: linear-gradient(90deg, var(--sky-blue), #35afe4 50%, var(--sky-blue));
  }
  .card--front .pattern-band--top { top: 0; height: 95px; }
  .card--front .pattern-band--bottom { top: 300px; height: 78px; }
  .card--back .pattern-band--top { top: 0; height: 83px; }
  .card--back .pattern-band--bottom { top: 299px; height: 79px; }

  .corner-triangle { position: absolute; left: 0; top: 0; width: 541px; height: 378px; }

  .brand-mark {
    position: absolute;
    display: flex; align-items: center; justify-content: center;
    border-radius: 50%;
    font-family: "Lato", sans-serif; font-weight: 900;
    letter-spacing: 0.03em;
  }
  .brand-mark--front {
    left: 47px; top: 47px; width: 129px; height: 129px;
    border: 5px solid var(--white);
    color: var(--white); font-size: 16px;
  }
  .brand-mark--back {
    left: 243px; top: 232px; width: 56px; height: 56px;
    border: 2px solid var(--ink-blue);
    color: var(--ink-blue); font-size: 7px;
  }

  .thank-you {
    position: absolute; left: 205px; top: 140px;
    font-family: "Great Vibes", cursive; font-weight: 400;
    font-size: 70px; line-height: 1;
    color: var(--sky-blue); white-space: nowrap;
  }

  .feedback {
    position: absolute; left: 0; top: 100px; width: 100%;
    text-align: center; color: var(--ink-blue);
  }
  .feedback__title {
    font-family: "Great Vibes", cursive; font-weight: 400;
    font-size: 31px; line-height: 1; margin-bottom: 10px;
  }
  .feedback__body {
    font-weight: 300; font-size: 12px; line-height: 22px;
  }
  .feedback__body strong { font-weight: 700; }
</style>
</head>
<body>
<main class="canvas">

  <section class="card card--front" aria-label="Front of insert">
    <div class="pattern-band pattern-band--top" role="img" aria-label="Snowflake pattern band"></div>
    <div class="pattern-band pattern-band--bottom" role="img" aria-label="Snowflake pattern band"></div>
    <svg class="corner-triangle" viewBox="0 0 541 378" aria-hidden="true">
      <polygon points="0,0 390,0 0,378" fill="var(--deep-blue)"/>
    </svg>
    <div class="brand-mark brand-mark--front">RIDGEWAY</div>
    <h1 class="thank-you">Thank You</h1>
  </section>

  <section class="card card--back" aria-label="Back of insert">
    <div class="pattern-band pattern-band--top" role="img" aria-label="Snowflake pattern band"></div>
    <div class="pattern-band pattern-band--bottom" role="img" aria-label="Snowflake pattern band"></div>
    <div class="feedback">
      <h2 class="feedback__title">We would love to hear your feedback!</h2>
      <p class="feedback__body">
        For every review we receive on our products, we donate 100% of the proceeds of your order<br>
        to <strong>TIDEWELL</strong> – a non profit organization dedicated to preserving our oceans! If you are not<br>
        100% satisfied with your purchase or have any problems, we will always resolve your issue.<br>
        please contact us via Brindle if you need assistance.
      </p>
    </div>
    <div class="brand-mark brand-mark--back">RIDGEWAY</div>
  </section>

</main>
</body>
</html>
```